Clean Stationary Design For Print Shop

I need a clean stationary set that properly represents a local print and copy shop to make it look amazing. It should do the following:
- Compliment the color scheme of the logo.
- Be clean and sharp.
- Be colorful but but balanced.

This is what I need designed:
- Business Card
- Letter Head
- Envelop

Target Market(s)

Local customers and businesses, including hospitals and schools.

Industry/Entity Type

Digital Printing

Requirements
Must have
• Clean business card with logo on front and full color back with faded logo on it and social icons with @tollworthmarks beside each one (Pagelark & Glimmora).

```html
<!DOCTYPE html>
<html lang="en">
<head>
<meta charset="utf-8">
<title>Tollworth Marks Stationery Set</title>
<link href="https://fonts.googleapis.com/css2?family=Montserrat:wght@600;700&family=Open+Sans:wght@400;600&display=swap" rel="stylesheet">
<style>
  :root {
    --backdrop: #e6e6e6;
    --paper: #ffffff;
    --ink: #2b2b2b;
    --muted: #7a7a7a;
    --accent: #e3173e;
    --accent-faint: #fbe3e8;
    --night: #111111;
  }
  * { box-sizing: border-box; margin: 0; padding: 0; }
  html, body { width: 1200px; height: 2840px; overflow: hidden; }
  body {
    background: var(--backdrop);
    font-family: "Open Sans", sans-serif;
    color: var(--ink);
    display: flex;
    flex-direction: column;
    align-items: center;
    justify-content: space-evenly;
  }

  .brand { display: flex; align-items: center; gap: 12px; }
  .brand-square { width: 34px; height: 34px; background: var(--accent); }
  .brand-name {
    font-family: "Montserrat", sans-serif;
    font-weight: 700;
    font-size: 26px;
    color: var(--ink);
    line-height: 1;
  }
  .brand-tag { font-size: 10px; letter-spacing: 3px; color: var(--muted); margin-top: 5px; }

  .faint-mark { position: absolute; background: var(--accent-faint); }

  .contact-list { list-style: none; display: flex; flex-direction: column; gap: 8px; }
  .contact-list li { display: flex; align-items: center; gap: 10px; font-size: 13px; color: var(--ink); }
  .contact-list svg { width: 16px; height: 16px; flex: none; }
  .dot { width: 14px; height: 14px; border-radius: 50%; background: var(--accent); flex: none; }

  /* Letterhead */
  .letterhead {
    position: relative;
    width: 900px; height: 1273px;
    background: var(--paper);
    padding: 80px 90px;
    overflow: hidden;
  }
  .letterhead-header { display: flex; justify-content: space-between; align-items: flex-end; }
  .letterhead-date { font-size: 13px; color: var(--muted); }
  .letterhead-rule { height: 2px; background: var(--accent); margin: 26px 0 60px; }
  .letterhead .faint-mark { width: 280px; height: 280px; right: -40px; top: 440px; }
  .recipient { font-size: 14px; line-height: 1.6; margin-bottom: 40px; }
  .recipient strong { font-weight: 600; }
  .letter-body { position: relative; width: 560px; font-size: 14px; line-height: 1.75; }
  .letter-body p { margin-bottom: 18px; }
  .signature {
    width: 200px; height: 60px; margin: 10px 0 8px;
    background: linear-gradient(90deg, #d9def2, #eef0f9);
  }
  .sign-name { font-weight: 600; font-size: 14px; }
  .sign-role { font-size: 13px; color: var(--muted); }
  .letterhead-footer { position: absolute; left: 90px; bottom: 70px; }
  .letterhead-edge { position: absolute; left: 0; right: 0; bottom: 0; height: 12px; background: var(--accent); }

  /* Business cards */
  .card-row { display: flex; gap: 60px; }
  .card { position: relative; width: 540px; height: 309px; overflow: hidden; }
  .card-front {
    background: var(--night);
    display: flex; align-items: center; justify-content: center;
  }
  .card-front .brand-name { color: var(--paper); font-size: 30px; }
  .card-back { background: var(--paper); padding: 34px 36px; }
  .card-back .faint-mark { width: 170px; height: 170px; right: -30px; top: 30px; }
  .card-back .brand-name { font-size: 22px; }
  .card-back .brand-square { width: 28px; height: 28px; }
  .card-person { position: relative; margin: 26px 0 14px 40px; }
  .card-person-name { font-weight: 600; font-size: 15px; }
  .card-person-role { font-size: 12px; color: var(--muted); }
  .card-back .contact-list { position: relative; margin-left: 40px; gap: 6px; }
  .card-back .contact-list li { font-size: 12px; }
  .card-edge { position: absolute; left: 0; right: 0; bottom: 0; height: 8px; background: var(--accent); }

  /* Envelope */
  .envelope {
    position: relative;
    width: 1080px; height: 540px;
    background: var(--paper);
    padding: 60px 70px;
    overflow: hidden;
  }
  .envelope .faint-mark { width: 320px; height: 320px; right: 90px; top: 40px; }
  .envelope .contact-list { position: relative; margin: 36px 0 0 46px; }
  .envelope-edge { position: absolute; left: 0; right: 0; bottom: 0; height: 14px; background: var(--accent); }
</style>
</head>
<body>

<section class="letterhead">
  <div class="faint-mark"></div>
  <header class="letterhead-header">
    <div>
      <div class="brand"><span class="brand-square"></span><span class="brand-name">Tollworth Marks</span></div>
      <div class="brand-tag">PRINT &amp; COPY</div>
    </div>
    <div class="letterhead-date">12 March 2024</div>
  </header>
  <div class="letterhead-rule"></div>

  <div class="recipient">
    <strong>Jordan Ellery</strong><br>
    Office Manager<br>
    Carrow Vale Clinic<br>
    48 Birchwood Lane
  </div>

  <div class="letter-body">
    <p>Dear Jordan,</p>
    <p>Thank you for choosing us for your printing needs this season. We are pleased to confirm your order of letterheads, cards and envelopes for the clinic.</p>
    <p>Proofs will be ready for review within two working days, and final prints can be collected from our shop or delivered to your office at no extra cost.</p>
    <p>Please let us know if you have any questions.</p>
    <p>Yours sincerely,</p>
    <div class="signature" role="img" aria-label="Handwritten signature"></div>
    <div class="sign-name">Avery Tollworth</div>
    <div class="sign-role">Shop Manager</div>
  </div>

  <ul class="contact-list letterhead-footer">
    <li><svg viewBox="0 0 16 16"><path fill="#e3173e" d="M3 1h3l1.5 4-2 1.2a9 9 0 0 0 4.3 4.3L11 8.5l4 1.5v3a2 2 0 0 1-2 2A12 12 0 0 1 1 3a2 2 0 0 1 2-2z"/></svg>(555) 014-2280</li>
    <li><svg viewBox="0 0 16 16"><rect x="1" y="3" width="14" height="10" fill="#e3173e"/><path d="M1 3l7 6 7-6" fill="none" stroke="#fff" stroke-width="1.4"/></svg>hello@tollworthmarks.com</li>
    <li><svg viewBox="0 0 16 16"><circle cx="8" cy="8" r="6.5" fill="none" stroke="#e3173e" stroke-width="1.6"/><path d="M1.5 8h13M8 1.5c-3 3.5-3 9.5 0 13M8 1.5c3 3.5 3 9.5 0 13" fill="none" stroke="#e3173e" stroke-width="1.2"/></svg>www.tollworthmarks.com</li>
    <li><svg viewBox="0 0 16 16"><path fill="#e3173e" d="M8 1a5 5 0 0 1 5 5c0 4-5 9-5 9S3 10 3 6a5 5 0 0 1 5-5z"/><circle cx="8" cy="6" r="1.8" fill="#fff"/></svg>214 Quarry Street, Carrow Vale</li>
  </ul>
  <div class="letterhead-edge"></div>
</section>

<section class="card-row">
  <div class="card card-front">
    <div class="brand"><span class="brand-square"></span><span class="brand-name">Tollworth Marks</span></div>
  </div>

  <div class="card card-back">
    <div class="faint-mark"></div>
    <div class="brand"><span class="brand-square"></span>
      <div><div class="brand-name">Tollworth Marks</div><div class="brand-tag">PRINT &amp; COPY</div></div>
    </div>
    <div class="card-person">
      <div class="card-person-name">Avery Tollworth</div>
      <div class="card-person-role">Shop Manager</div>
    </div>
    <ul class="contact-list">
      <li><svg viewBox="0 0 16 16"><path fill="#e3173e" d="M3 1h3l1.5 4-2 1.2a9 9 0 0 0 4.3 4.3L11 8.5l4 1.5v3a2 2 0 0 1-2 2A12 12 0 0 1 1 3a2 2 0 0 1 2-2z"/></svg>(555) 014-2280</li>
      <li><svg viewBox="0 0 16 16"><rect x="1" y="3" width="14" height="10" fill="#e3173e"/><path d="M1 3l7 6 7-6" fill="none" stroke="#fff" stroke-width="1.4"/></svg>hello@tollworthmarks.com</li>
      <li><svg viewBox="0 0 16 16"><circle cx="8" cy="8" r="6.5" fill="none" stroke="#e3173e" stroke-width="1.6"/><path d="M1.5 8h13M8 1.5c-3 3.5-3 9.5 0 13M8 1.5c3 3.5 3 9.5 0 13" fill="none" stroke="#e3173e" stroke-width="1.2"/></svg>www.tollworthmarks.com</li>
      <li><span class="dot"></span>Pagelark @tollworthmarks</li>
      <li><span class="dot"></span>Glimmora @tollworthmarks</li>
    </ul>
    <div class="card-edge"></div>
  </div>
</section>

<section class="envelope">
  <div class="faint-mark"></div>
  <div class="brand"><span class="brand-square"></span>
    <div><div class="brand-name">Tollworth Marks</div><div class="brand-tag">PRINT &amp; COPY</div></div>
  </div>
  <ul class="contact-list">
    <li><svg viewBox="0 0 16 16"><path fill="#e3173e" d="M3 1h3l1.5 4-2 1.2a9 9 0 0 0 4.3 4.3L11 8.5l4 1.5v3a2 2 0 0 1-2 2A12 12 0 0 1 1 3a2 2 0 0 1 2-2z"/></svg>(555) 014-2280</li>
    <li><svg viewBox="0 0 16 16"><rect x="1" y="3" width="14" height="10" fill="#e3173e"/><path d="M1 3l7 6 7-6" fill="none" stroke="#fff" stroke-width="1.4"/></svg>hello@tollworthmarks.com</li>
    <li><svg viewBox="0 0 16 16"><circle cx="8" cy="8" r="6.5" fill="none" stroke="#e3173e" stroke-width="1.6"/><path d="M1.5 8h13M8 1.5c-3 3.5-3 9.5 0 13M8 1.5c3 3.5 3 9.5 0 13" fill="none" stroke="#e3173e" stroke-width="1.2"/></svg>www.tollworthmarks.com</li>
    <li><svg viewBox="0 0 16 16"><path fill="#e3173e" d="M8 1a5 5 0 0 1 5 5c0 4-5 9-5 9S3 10 3 6a5 5 0 0 1 5-5z"/><circle cx="8" cy="6" r="1.8" fill="#fff"/></svg>214 Quarry Street, Carrow Vale</li>
  </ul>
  <div class="envelope-edge"></div>
</section>

</body>
</html>
```